Tarvolink - Smart Border Flow Reshaping Trade

Web Design for international start-up, which is automating customs clearance processes for forwarding companies by applying a web application, which is operating with artificial intelligence and robotic process automation. Tarvolink pursues the vision of supporting forwarding companies successfully in becoming digital masters and co-creates innovative software solutions with all participants (ex- and importers of goods) along value-added chains. With intelligent/smart/digital customs clearance software or in other words, a virtual customs clearance roboter tailord to the customers needs, we are transforming businesses. The website could look like this:

https://www.qorvanta.example/uk-en/index.php
or
https://pagelumen.example/theme/brindlemoor

Please use colours and designs you think would be the best fit. These websites are just here to give you an idea of how the webdesign could look like. Use the attached logo design as a basis for further web design. You can use the provided pictures, but you can also use your own ones, if you think they are better suited. But please take care, that they have a high resolution quality.

Description of Website: The website is transparent and modern. It provides seven pages such as homepage, products, web app, the about us, working at Tarvolink, News, contact us and search results page. The homepage or landing page should be filled with a short description of the company, what Tarvolink is doing, how they will support its customers and will also include a video of the provided solution. Products provide obviously information about different products and their characteristics. Web app page includes information about principles and technologies that get the software going. The about us page includes unique advantages and value propositions for customers and the contact us, as the name already says, will provide contact information and possibilities to contact us. The rest is also obvious (for additional information look up the website of QVT, priorly provided link - the page is also available in english).

If you have any questions, I am happy to answer them any time.
Updates

I have to think about the text that I want to have included into the design and hadn't have the time to compose it.

Target Market(s)

Forwarding Companies, Ex-/Importers

Industry/Entity Type

It Company

Number of Pages Required

5+ page

Requirements
Must have
• The web design should be designes according to the attached logo of Tarvolink.

```html
<!DOCTYPE html>
<html lang="en">
<head>
<meta charset="utf-8">
<title>Tarvolink – Smart Border Flow Reshaping Trade</title>
<link href="https://fonts.googleapis.com/css2?family=Raleway:wght@400;500;600;700&display=swap" rel="stylesheet">
<style>
:root{
  --blue:#1aaed8;
  --blue-deep:#3a4aa6;
  --indigo:#3b3f9e;
  --ink:#1d1d1f;
  --text:#555a66;
  --grey:#f3f3f3;
  --white:#ffffff;
  --rule:#1aa3d6;
}
*{box-sizing:border-box;margin:0;padding:0}
html,body{width:1200px;height:4240px;overflow:hidden}
body{font-family:'Raleway',sans-serif;color:var(--text);background:var(--white);position:relative}
.abs{position:absolute}
.brand{font-family:'Raleway',sans-serif;font-weight:600;color:var(--blue);letter-spacing:1px}
.brand-mark{display:inline-block;width:14px;height:14px;background:var(--blue);border-radius:50%;margin-right:10px;vertical-align:middle}

/* header */
.topbar{left:0;top:0;width:1200px;height:88px;background:var(--white)}
.topbar .brand{position:absolute;left:157px;top:20px;font-size:40px}
.topbar .tagline{position:absolute;left:262px;top:63px;font-size:11px;color:var(--indigo)}
.contact{position:absolute;top:28px;font-size:11px;color:var(--ink);line-height:17px}
.contact b{font-weight:700}
.contact svg{position:absolute;left:-40px;top:4px}
.social-top{position:absolute;left:918px;top:36px;display:flex;gap:16px}
.social-top span{width:14px;height:14px;border-radius:50%;background:#7a7f88}

.navbar{left:0;top:88px;width:1200px;height:52px;background:linear-gradient(90deg,var(--blue),var(--blue-deep))}
.navbar ul{list-style:none;display:flex;position:absolute;left:170px;top:19px;gap:0}
.navbar li{color:var(--white);font-size:12px;margin-right:46px}
.search{position:absolute;left:888px;top:10px;width:157px;height:31px;background:var(--white);border-radius:4px;font-size:10px;color:#b5b9c0;padding:10px 16px}
.search svg{position:absolute;right:8px;top:9px}

/* hero */
.hero{left:0;top:140px;width:1200px;height:537px;background:linear-gradient(180deg,#5f6a73 0%,#8c959b 35%,#4c7f8c 62%,#2f6576 100%)}
.hero-text{position:absolute;left:0;width:1200px;text-align:center;color:var(--white)}
.hero h1{top:185px;font-size:64px;font-weight:600}
.hero h2{top:258px;font-size:33px;font-weight:600}
.hero p{top:308px;font-size:12px}
.dots{position:absolute;left:565px;top:468px;display:flex;gap:6px}
.dots i{width:9px;height:9px;border-radius:50%;background:rgba(255,255,255,.6)}
.dots i.on{background:var(--white)}

/* partners */
.partners{left:0;top:677px;width:1200px;height:168px;background:var(--grey)}
.badge{position:absolute;border-radius:4px}

/* about */
.about-art{left:175px;top:880px;width:330px;height:370px;background:linear-gradient(135deg,#e6f3fa,#bcdff0);border-radius:6px}
.about h3{position:absolute;left:546px;top:910px;font-size:31px;font-weight:600;color:var(--ink)}
.about p{position:absolute;left:546px;top:978px;width:480px;font-size:11px;line-height:25.6px;color:var(--text)}
.btn{position:absolute;background:linear-gradient(90deg,var(--blue),var(--blue-deep));color:var(--white);font-size:11px;border-radius:5px;text-align:center}

/* features */
.features-title{left:0;top:1432px;width:1200px;text-align:center;color:var(--white);font-size:30px;font-weight:600;line-height:42px}
.rule{position:absolute;height:4px;width:80px;background:var(--rule)}
.rule.white{background:var(--white)}
.feature{position:absolute;top:1600px;width:260px;text-align:center;color:var(--white)}
.feature h4{margin-top:78px;font-size:19px;font-weight:600}
.feature p{margin-top:22px;font-size:11px;line-height:21px;color:#dce6f5}
.feature .chev{margin-top:18px}

/* video */
.section-title{left:0;width:1200px;text-align:center;font-size:31px;font-weight:600;color:var(--ink)}
.doing-text{left:230px;top:2146px;width:740px;text-align:center;font-size:11px;line-height:25px}
.video{left:141px;top:2223px;width:917px;height:505px;background:radial-gradient(ellipse at center,#1d2c3a 0%,#0e1822 70%);border-radius:6px;box-shadow:0 6px 18px rgba(0,0,0,.25)}
.play{position:absolute;left:427px;top:232px;width:62px;height:42px;border-radius:10px;background:#e52d27}
.play::after{content:"";position:absolute;left:25px;top:12px;border-left:16px solid #fff;border-top:9px solid transparent;border-bottom:9px solid transparent}

/* news */
.news-bg{left:0;top:2795px;width:1200px;height:620px;background:var(--grey)}
.card{position:absolute;top:2948px;width:290px}
.card .photo{height:200px}
.card .date{position:absolute;left:35px;top:185px;width:98px;height:30px;background:linear-gradient(90deg,var(--blue),var(--blue-deep));color:#fff;font-size:11px;text-align:center;line-height:30px}
.card h5{margin:40px 0 0 28px;font-size:23px;font-weight:600;color:var(--ink)}
.card p{margin:22px 0 0 28px;width:240px;font-size:11px;line-height:25px}
.card a{display:block;margin:14px 0 0 28px;font-size:11px;color:var(--blue);text-decoration:underline}

/* testimonials */
.testi-photo{left:190px;top:3560px;width:258px;height:232px;border-radius:48% 52% 46% 54%/52% 44% 56% 48%;background:linear-gradient(135deg,#c9d6dc,#6f8793)}
.quote{left:520px;top:3610px;width:510px;font-size:11px;line-height:31px;color:var(--white)}
.person{left:520px;top:3722px;color:var(--white)}
.person b{display:block;font-size:17px;font-weight:600}
.person span{font-size:11px}
.arrow{position:absolute;top:3818px;width:33px;height:33px;border-radius:50%;background:var(--white)}

/* footer */
.footer-brand{left:0;top:3955px;width:1200px;text-align:center}
.footer-brand .brand{font-size:60px}
.footer-brand .tagline{display:block;font-size:15px;color:var(--indigo);margin-left:170px;margin-top:-8px}
.footer-nav{left:0;top:4076px;width:1200px;display:flex;justify-content:center;list-style:none}
.footer-nav li{font-size:12px;color:var(--ink);margin:0 24px}
.footer-line{left:141px;top:4140px;width:917px;height:1px;background:#333}
.footer-social{left:520px;top:4126px;display:flex;gap:12px;background:var(--white);padding:0 8px}
.footer-social span{width:28px;height:28px;border:1.5px solid #222;border-radius:50%}
.copyright{left:0;top:4200px;width:1200px;text-align:center;font-size:11px;color:var(--ink)}
</style>
</head>
<body>

<header class="abs topbar">
  <div class="brand"><span class="brand-mark"></span>Tarvolink</div>
  <div class="tagline">Smart Border Flow</div>
  <div class="contact" style="left:607px">
    <svg width="20" height="20" viewBox="0 0 24 24" fill="none" stroke="#555" stroke-width="1.5"><path d="M5 3h4l2 5-3 2a12 12 0 0 0 6 6l2-3 5 2v4a2 2 0 0 1-2 2A17 17 0 0 1 3 5a2 2 0 0 1 2-2z"/></svg>
    <b>Call Us!</b><br>00-000-0000
  </div>
  <div class="contact" style="left:766px">
    <svg width="22" height="16" viewBox="0 0 24 16" fill="none" stroke="#555" stroke-width="1.5"><rect x="1" y="1" width="22" height="14"/><path d="M1 1l11 8 11-8"/></svg>
    <b>Email Us!</b><br>info@tarvolink.example
  </div>
  <div class="social-top"><span></span><span></span><span></span></div>
</header>

<nav class="abs navbar">
  <ul><li>Home</li><li>Products</li><li>Web app</li><li>About us</li><li>Working at Tarvolink</li><li>News</li><li>Contact us</li></ul>
  <div class="search">Search...
    <svg width="13" height="13" viewBox="0 0 14 14" fill="none" stroke="#999" stroke-width="1.4"><circle cx="6" cy="6" r="4.5"/><path d="M9.5 9.5L13 13"/></svg>
  </div>
</nav>

<section class="abs hero" role="img" aria-label="Modern white architecture reflected in a calm pool under a cloudy sky">
  <h1 class="hero-text">Smart Border Flow</h1>
  <h2 class="hero-text">Reshaping Trade</h2>
  <p class="hero-text">Tarvolink pursues the vision of supporting forwarding companies successfully in becoming digital masters</p>
  <div class="dots"><i></i><i></i><i class="on"></i><i></i><i></i></div>
</section>

<section class="abs partners">
  <div class="badge" style="left:158px;top:42px;width:275px;height:85px;background:#e2e2e2" role="img" aria-label="Partner badge"></div>
  <div class="badge" style="left:468px;top:42px;width:424px;height:85px;background:#d5e4f2" role="img" aria-label="Partner badge"></div>
  <div class="badge" style="left:945px;top:36px;width:82px;height:92px;background:#2b3585" role="img" aria-label="Partner badge"></div>
</section>

<section class="about">
  <div class="abs about-art" role="img" aria-label="Large circuit-style brand illustration"></div>
  <h3>About Us</h3>
  <p>Sed ut perspiciatis unde omnis iste natus error sit voluptatem accusantium doloremque laudantium, totam rem aperiam, eaque ipsa quae ab illo inventore veritatis et quasi architecto beatae vitae dicta sunt explicabo. Nemo enim ipsam voluptatem quia voluptas sit aspernatur aut odit aut fugit, sed quia consequuntur magni dolores eos qui ratione voluptatem sequi nesciunt. Neque porro quisquam est, qui dolorem ipsum quia dolor sit amet, consectetur, adipisci velit, sed quia non numquam eius modi tempora incidunt ut labore et dolore magnam aliquam quaerat voluptatem.</p>
  <div class="btn" style="left:546px;top:1201px;width:100px;height:33px;line-height:33px">Learn More</div>
</section>

<svg class="abs" style="left:0;top:1320px" width="1200" height="680" viewBox="0 0 1200 680">
  <defs>
    <linearGradient id="featGrad" x1="0" y1="0" x2="0" y2="1">
      <stop offset="0" stop-color="#1aaed8"/><stop offset="1" stop-color="#3b3f9e"/>
    </linearGradient>
  </defs>
  <path d="M0 95 C300 0 700 -20 1200 20 L1200 540 C900 640 400 700 0 640 Z" fill="#000"/>
  <path d="M0 110 C300 30 700 10 1200 40 L1200 520 C900 630 400 690 0 660 Z" fill="url(#featGrad)"/>
</svg>

<h2 class="abs features-title">Tarvolink Software Revolutionizing<br>Customs Management</h2>
<div class="rule white" style="left:560px;top:1530px"></div>

<div class="feature" style="left:156px">
  <svg width="70" height="64" viewBox="0 0 70 64" fill="none" stroke="#fff" stroke-width="1.6"><path d="M14 4h8l10 46"/><rect x="26" y="14" width="20" height="16" transform="rotate(-12 36 22)"/><rect x="30" y="30" width="22" height="14" transform="rotate(-12 41 37)"/><circle cx="34" cy="56" r="5"/><path d="M38 54l22-5"/></svg>
  <h4>What Tarvolink is doing</h4>
  <p>Sed ut perspiciatis unde omnis iste natus error sit voluptatem accusantium doloremque laudantium, totam rem aperiam</p>
  <svg class="chev" width="24" height="22" viewBox="0 0 24 22" fill="none" stroke="#fff" stroke-width="2.5"><path d="M3 3l9 8 9-8M3 11l9 8 9-8"/></svg>
</div>
<div class="feature" style="left:466px">
  <svg width="70" height="64" viewBox="0 0 70 64" fill="none" stroke="#fff" stroke-width="1.6"><path d="M10 52l14-14 8 8-14 14zM24 38l10-16 14-8 10 10-8 14-16 10"/><path d="M34 22l12 12M40 18l12 12"/></svg>
  <h4>How they will support</h4>
  <p>Sed ut perspiciatis unde omnis iste natus error sit voluptatem accusantium doloremque laudantium, totam rem aperiam</p>
  <svg class="chev" width="24" height="22" viewBox="0 0 24 22" fill="none" stroke="#fff" stroke-width="2.5"><path d="M3 3l9 8 9-8M3 11l9 8 9-8"/></svg>
</div>
<div class="feature" style="left:776px">
  <svg width="70" height="64" viewBox="0 0 70 64" fill="none" stroke="#fff" stroke-width="1.6"><path d="M10 6h20v8a5 5 0 0 1 0 10v8H10zM30 6h20v20h-8a5 5 0 0 0-10 0"/><path d="M34 34h24v24H34z"/></svg>
  <h4>Provided solution</h4>
  <p>Sed ut perspiciatis unde omnis iste natus error sit voluptatem accusantium doloremque laudantium, totam rem aperiam</p>
  <svg class="chev" width="24" height="22" viewBox="0 0 24 22" fill="none" stroke="#fff" stroke-width="2.5"><path d="M3 3l9 8 9-8M3 11l9 8 9-8"/></svg>
</div>

<h2 class="abs section-title" style="top:2050px">What Tarvolink is doing</h2>
<div class="rule" style="left:560px;top:2110px"></div>
<p class="abs doing-text">Sed ut perspiciatis unde omnis iste natus error sit voluptatem accusantium doloremque laudantium, totam rem aperiam, eaque ipsa quae ab illo inventore veritatis et quasi architecto beatae vitae dicta sunt explicabo.</p>
<div class="abs video" role="img" aria-label="Video still: aerial view of a cargo tanker on dark sea">
  <div class="play"></div>
</div>

<div class="abs news-bg"></div>
<h2 class="abs section-title" style="top:2852px">Latest News</h2>
<div class="rule" style="left:564px;top:2912px;width:72px"></div>

<article class="card" style="left:141px">
  <div class="photo" role="img" aria-label="Harbour cranes at sunset" style="background:linear-gradient(180deg,#5b6f86,#d89a5a 60%,#2c3a48)"></div>
  <div class="date">07.05.2019</div>
  <h5>Sed ut perspiciatis</h5>
  <p>Sed ut perspiciatis unde omnis iste natus error sit voluptatem accusantium doloremque laudantium, totam rem</p>
  <a>Read More</a>
</article>
<article class="card" style="left:454px">
  <div class="photo" role="img" aria-label="Futuristic building lit in blue at night" style="background:radial-gradient(ellipse at center,#1a7fd0 0%,#0d2c5c 55%,#050a18 100%)"></div>
  <div class="date">07.05.2019</div>
  <h5>Sed ut perspiciatis</h5>
  <p>Sed ut perspiciatis unde omnis iste natus error sit voluptatem accusantium doloremque laudantium, totam rem</p>
  <a>Read More</a>
</article>
<article class="card" style="left:768px">
  <div class="photo" role="img" aria-label="White modern architecture under a blue sky" style="background:linear-gradient(180deg,#4f7fc0,#a9c6e4 55%,#d8dde0)"></div>
  <div class="date">07.05.2019</div>
  <h5>Sed ut perspiciatis</h5>
  <p>Sed ut perspiciatis unde omnis iste natus error sit voluptatem accusantium doloremque laudantium, totam rem</p>
  <a>Read More</a>
</article>

<svg class="abs" style="left:0;top:3370px" width="1200" height="580" viewBox="0 0 1200 580">
  <defs>
    <linearGradient id="testiGrad" x1="0" y1="0" x2="0" y2="1">
      <stop offset="0" stop-color="#1aaed8"/><stop offset="1" stop-color="#3b3f9e"/>
    </linearGradient>
  </defs>
  <path d="M0 0 C400 40 800 40 1200 0 L1200 565 C800 500 400 500 0 565 Z" fill="url(#testiGrad)"/>
</svg>

<h2 class="abs section-title" style="top:3472px;color:#fff">Testimonials</h2>
<div class="rule white" style="left:560px;top:3530px"></div>
<div class="abs testi-photo" role="img" aria-label="Portrait of a client"></div>
<p class="abs quote">Lorem ipsum dolor sit amet, consectetur adipisicing elit, sed do eiusmod tempor incididunt ut labore et dolore magna aliqua. Ut enim ad minim veniam, quis nostrud exercitation ullamco laboris nisi ut aliquip ex ea commodo consequat.</p>
<div class="abs person"><b>Marek Lindqvist</b><span>Position / Company Name</span></div>
<div class="arrow" style="left:922px"><svg width="33" height="33" viewBox="0 0 33 33" fill="none" stroke="#3b3f9e" stroke-width="1.6"><path d="M19 11l-5 5.5 5 5.5"/></svg></div>
<div class="arrow" style="left:970px"><svg width="33" height="33" viewBox="0 0 33 33" fill="none" stroke="#3b3f9e" stroke-width="1.6"><path d="M14 11l5 5.5-5 5.5"/></svg></div>

<footer>
  <div class="abs footer-brand"><span class="brand"><span class="brand-mark" style="width:18px;height:18px"></span>Tarvolink</span><span class="tagline">Smart Border Flow</span></div>
  <ul class="abs footer-nav"><li>Home</li><li>Products</li><li>Web app</li><li>About us</li><li>Working at Tarvolink</li><li>News</li><li>Contact us</li></ul>
  <div class="abs footer-line"></div>
  <div class="abs footer-social"><span></span><span></span><span></span><span></span></div>
  <p class="abs copyright">© Copyright 2019 Tarvolink Smart Border Flow All Right Reserved</p>
</footer>

</body>
</html>
```